FoldKite App for On-Demand Laundry

We are launching a startup of online laundry service using mobile app. This startup will give the most convenient experience for the customers in managing their laundry. In only few taps away with the app, we'll send our agents to pick up laundry at the customer's doorstep, proceed it as per their order type, and get it delivered back to them in a schedule that fits them well.

We need somebody that can help with us and make our app as one of the simplest yet most effective app to use, design should be clean and easy to navigate, leave experience that makes our users want to come back and use it again. It will consist of key features that the app should have as follows:

- Sign up & Login
- Add customer address
- Schedule laundry pick up & delivery
- Laundry service selection
- Confirmation and Payment
- Status Tracking

Please refer to the attachment for details of business flows. Example of apps that can inspire: Rinsely, Sudzoria, Presqo.

--PLEASE DO NOT USE THE LOGO FROM ATTACHMENT, IT'S ONLY A DUMMY LOGO--
Updates

Target Market(s)

Young Professional, College Students, Young Early Family

Industry/Entity Type

Cleaning Service

Font styles to use
Sans Serif

Colors
ffffff
9d9d9d
0392cd
33a6d7
86cfc6
33b8a4
acd036
cadf82

Requirements
Must have
• Simplicity and elegance. Clean and easy navigation.
• Example from attachment is "ugly" but can tell the overall idea on what information to capture from the app. We need to get a completely different design which is way better than it.
Nice to have
• Inspiration could be from similar apps like: Rinsely, Sudzoria, and Presqo.
Should not have
• --PLEASE DO NOT USE THE LOGO FROM ATTACHMENT, IT'S ONLY A DUMMY LOGO--

```html
<!DOCTYPE html>
<html lang="en">
<head>
<meta charset="utf-8">
<title>FoldKite – Schedule Pick Up</title>
<link rel="stylesheet" href="https://fonts.googleapis.com/css2?family=Roboto+Condensed:wght@300;400&family=Roboto:wght@400&display=swap">
<style>
  :root {
    --brand-blue: #2f86e8;
    --brand-blue-deep: #1f74dc;
    --white: #ffffff;
    --ink: #25384a;
    --muted: #a7adb3;
    --hairline: #e4e7ea;
    --dot-active: #9fd3ea;
    --dot-idle: #ececee;
    --tabbar: #f3f6f9;
    --icon: #8d959c;
  }
  * { box-sizing: border-box; margin: 0; padding: 0; }
  html, body { width: 745px; height: 1200px; overflow: hidden; background: var(--white); }
  body { font-family: "Roboto Condensed", sans-serif; color: var(--ink); }

  .screen { position: relative; width: 745px; height: 1200px; background: var(--white); overflow: hidden; }

  .header-photo {
    position: absolute; left: 0; top: 0; width: 745px; height: 335px;
    background: linear-gradient(180deg, #3a8ff0 0%, var(--brand-blue) 45%, var(--brand-blue-deep) 100%);
  }

  .status-bar {
    position: absolute; left: 0; top: 0; width: 100%; height: 44px;
    font-family: "Roboto", sans-serif; font-size: 20px; color: var(--white);
  }
  .status-left { position: absolute; left: 22px; top: 10px; display: flex; align-items: center; gap: 8px; }
  .status-time { position: absolute; left: 0; right: 0; top: 10px; text-align: center; }
  .status-right { position: absolute; right: 22px; top: 10px; display: flex; align-items: center; gap: 8px; }

  .brand-name {
    position: absolute; left: 0; right: 0; top: 56px; text-align: center;
    font-family: "Roboto Condensed", sans-serif; font-weight: 300; font-size: 40px;
    letter-spacing: 1px; color: var(--white);
  }

  .clock-badge {
    position: absolute; left: 227px; top: 186px; width: 290px; height: 290px; border-radius: 50%;
    background: var(--white); box-shadow: 0 4px 10px rgba(0,0,0,0.06);
    display: flex; align-items: center; justify-content: center;
  }

  .page-title {
    position: absolute; left: 0; right: 0; top: 508px; text-align: center;
    font-size: 34px; font-weight: 400; color: var(--ink);
  }

  .field {
    position: absolute; height: 58px; border: 2px solid var(--hairline); border-radius: 29px;
    display: flex; align-items: center; justify-content: space-between; padding: 0 24px;
    font-size: 25px;
  }
  .field-label { color: var(--muted); font-weight: 300; }
  .field-value { color: var(--ink); display: flex; align-items: center; gap: 14px; }
  .field-where { left: 56px; top: 633px; width: 647px; }
  .field-date { left: 56px; top: 766px; width: 282px; }
  .field-time { left: 420px; top: 766px; width: 283px; }

  .add-address {
    position: absolute; right: 92px; top: 696px; font-size: 17px; font-weight: 300; color: var(--muted);
  }

  .note-field {
    position: absolute; left: 60px; top: 896px; width: 626px; height: 44px;
    border-bottom: 2px solid var(--hairline); padding-left: 22px;
    font-size: 25px; font-weight: 300; color: var(--muted);
  }

  .pager { position: absolute; left: 0; right: 0; top: 1010px; display: flex; justify-content: center; gap: 30px; }
  .pager-dot { width: 29px; height: 29px; border-radius: 50%; background: var(--dot-idle); }
  .pager-dot.is-active { background: var(--dot-active); }

  .tab-bar {
    position: absolute; left: 0; bottom: 0; width: 100%; height: 93px; background: var(--tabbar);
    display: flex; justify-content: space-around; align-items: center; padding: 0 40px;
  }
</style>
</head>
<body>
<main class="screen">
  <div class="header-photo" role="img" aria-label="Blue-tinted photo of a laundry room with folded towels on shelves"></div>

  <div class="status-bar">
    <div class="status-left">
      <svg width="56" height="14" viewBox="0 0 56 14" aria-hidden="true">
        <circle cx="6" cy="7" r="5" fill="#fff"/><circle cx="17" cy="7" r="5" fill="#fff"/><circle cx="28" cy="7" r="5" fill="#fff"/>
        <circle cx="39" cy="7" r="4.3" fill="none" stroke="#fff" stroke-width="1.3"/><circle cx="50" cy="7" r="4.3" fill="none" stroke="#fff" stroke-width="1.3"/>
      </svg>
      <span>VOLTA</span>
      <svg width="22" height="16" viewBox="0 0 22 16" aria-hidden="true" fill="none" stroke="#fff" stroke-width="2" stroke-linecap="round">
        <path d="M2 5.5a13 13 0 0 1 18 0"/><path d="M5.5 9a8 8 0 0 1 11 0"/><circle cx="11" cy="13" r="1.4" fill="#fff" stroke="none"/>
      </svg>
    </div>
    <div class="status-time">4:21 PM</div>
    <div class="status-right">
      <svg width="12" height="20" viewBox="0 0 12 20" aria-hidden="true" fill="none" stroke="#fff" stroke-opacity="0.7" stroke-width="1.5">
        <path d="M1 5l10 9-5 5V1l5 5-10 9"/>
      </svg>
      <span>100%</span>
      <svg width="46" height="18" viewBox="0 0 46 18" aria-hidden="true">
        <rect x="1" y="1" width="40" height="16" rx="3" fill="none" stroke="#fff" stroke-width="1.5"/>
        <rect x="3" y="3" width="36" height="12" rx="1.5" fill="#fff"/>
        <rect x="42" y="6" width="3" height="6" rx="1" fill="#fff"/>
      </svg>
    </div>
  </div>

  <div class="brand-name">FoldKite</div>

  <div class="clock-badge">
    <svg width="150" height="150" viewBox="0 0 150 150" aria-hidden="true" fill="none" stroke="var(--brand-blue)" stroke-linecap="round">
      <circle cx="75" cy="75" r="69" stroke-width="4.5"/>
      <path d="M75 14v9M75 127v9M14 75h9M127 75h9" stroke-width="3.5"/>
      <path d="M75 75L46 59M75 75l27-39" stroke-width="4.5"/>
    </svg>
  </div>

  <h1 class="page-title">Schedule Pick Up</h1>

  <div class="field field-where">
    <span class="field-label">Where</span>
    <span class="field-value">Jalan Melati Indah apt 9
      <svg width="14" height="10" viewBox="0 0 14 10" aria-hidden="true"><path d="M0 0h14L7 10z" fill="#d7dbdf"/></svg>
    </span>
  </div>
  <div class="add-address">Add another address?</div>

  <div class="field field-date">
    <span class="field-label">Date</span>
    <span class="field-value">16.3.2015</span>
  </div>
  <div class="field field-time">
    <span class="field-label">Time</span>
    <span class="field-value">1 pm</span>
  </div>

  <div class="note-field">Optional Note</div>

  <div class="pager">
    <span class="pager-dot is-active"></span>
    <span class="pager-dot"></span>
    <span class="pager-dot"></span>
  </div>

  <nav class="tab-bar">
    <svg width="56" height="56" viewBox="0 0 56 56" aria-label="Clothes" fill="none" stroke="var(--icon)" stroke-width="1.6" stroke-linejoin="round">
      <path d="M20 5l-13 7 4 12 6-3v30h22V21l6 3 4-12-13-7c-2 4-5 6-8 6s-6-2-8-6z"/>
      <path d="M23 6l5 7 5-7"/>
    </svg>
    <svg width="62" height="50" viewBox="0 0 62 50" aria-label="Wallet" fill="none" stroke="var(--icon)" stroke-width="1.6">
      <rect x="2" y="3" width="58" height="44" rx="3"/>
      <path d="M2 10h58"/>
      <rect x="42" y="20" width="18" height="14" rx="2"/>
      <circle cx="50" cy="27" r="2.5"/>
    </svg>
    <svg width="56" height="56" viewBox="0 0 56 56" aria-label="Offers" fill="none" stroke="var(--icon)" stroke-width="1.6" stroke-linejoin="round">
      <path d="M30 8h16v16L22 48 6 32z"/>
      <circle cx="39" cy="15" r="3"/>
      <path d="M39 12c0-6 8-8 10-3"/>
    </svg>
    <svg width="56" height="56" viewBox="0 0 56 56" aria-label="Settings" fill="none" stroke="var(--icon)" stroke-width="1.6" stroke-linejoin="round">
      <path d="M24 4h8l1.5 6.5 4 2.3 6.4-2 4 7-5 4.5v4.4l5 4.5-4 7-6.4-2-4 2.3L32 52h-8l-1.5-6.5-4-2.3-6.4 2-4-7 5-4.5v-4.4l-5-4.5 4-7 6.4 2 4-2.3z"/>
      <circle cx="28" cy="28" r="7"/>
    </svg>
  </nav>
</main>
</body>
</html>
```